Web Design Project for Qolvine Enterprises

Qolvine Enterprises is a small company with expertise in manufacturing, product development, global sourcing and retail. We provide sales/broker, import/export, private label and product development services to both manufacturers and retailers of food, beverage, health and beauty care and general merchandise. Would like a web site that incorporates images that inspire confidence in the areas of international trade and product development as well as convey the experience of founder and CEO in these areas.

Own web address qolvineenterprises.net and have hosting from brimport.com

Target Market(s)

Retail and manufacturing professionals.

Industry/Entity Type

It Company

Font styles to use
Serif
Sans Serif

Requirements
Must have
• Tabs for: Home, About Us, Services, Contact Us

```html
<!DOCTYPE html>
<html lang="en">
<head>
<meta charset="utf-8">
<title>Qolvine Enterprises</title>
<link rel="stylesheet" href="https://fonts.googleapis.com/css2?family=Montserrat:wght@400;500;600&family=Arimo:wght@400;700&display=swap">
<style>
:root{
  --navy:#0b4f9e;
  --sky:#7ab8e3;
  --ink:#2e3b4e;
  --heading:#4a5566;
  --muted:#555e6b;
  --pale:#e9edf3;
  --white:#ffffff;
  --caption:rgba(20,28,40,.82);
}
*{margin:0;padding:0;box-sizing:border-box}
html,body{width:814px;height:1200px;overflow:hidden;background:var(--white)}
body{position:relative;font-family:Arimo,Arial,sans-serif;color:var(--muted)}
.abs{position:absolute}
.head-font{font-family:Montserrat,Arial,sans-serif}

/* header */
.brand{left:76px;top:16px;display:flex;align-items:center;gap:8px}
.brand-dot{width:34px;height:34px;border-radius:50%;background:var(--navy)}
.brand-name{font-family:Montserrat,sans-serif;font-weight:600;font-size:17px;color:var(--navy)}
.main-nav{right:84px;top:28px;display:flex;gap:19px;font-family:Montserrat,sans-serif;font-weight:500;font-size:10px}
.main-nav a{text-decoration:none;color:var(--navy)}
.main-nav a.current{color:#222}

/* hero */
.sky-band{left:0;top:82px;width:814px;height:305px;background:var(--sky)}
.hero-frame{left:74px;top:64px;width:666px;height:300px;background:var(--white);box-shadow:0 8px 6px -4px rgba(20,40,70,.35)}
.hero-photo{left:81px;top:64px;width:652px;height:294px;background:linear-gradient(135deg,#cfe0e6 0%,#a9c3cc 35%,#5d6a72 65%,#2b2f36 100%)}
.hero-caption{left:81px;top:311px;width:652px;height:47px;background:var(--caption)}
.hero-title{left:106px;top:322px;color:var(--white);font-family:Montserrat,sans-serif;font-weight:500;font-size:13px}
.hero-text{left:106px;top:340px;color:var(--white);font-size:8px}
.learn-btn{left:622px;top:320px;width:87px;height:31px;background:var(--navy);color:var(--white);font-family:Montserrat,sans-serif;font-weight:600;font-size:9px;display:flex;align-items:center;justify-content:center}

/* services */
.services{left:0;top:387px;width:814px;height:141px;background:var(--navy)}
.service{position:absolute;top:24px;width:196px;text-align:center;color:var(--white)}
.service svg{display:block;margin:0 auto 6px}
.service h3{font-family:Montserrat,sans-serif;font-weight:500;font-size:11px;margin-bottom:8px}
.service p{font-size:7.5px;line-height:10px;text-align:left}

/* news */
.news{left:0;top:528px;width:814px;height:298px;background:var(--pale)}
.news-title{left:95px;top:557px;font-family:Montserrat,sans-serif;font-size:20px;color:var(--heading)}
.news-more{left:665px;top:569px;font-size:9px;color:var(--navy)}
.news-rule{left:95px;top:585px;width:619px;height:1px;background:#8a94a3}
.news-item{position:absolute;width:290px;height:80px}
.date-ring{position:absolute;left:0;top:0;width:50px;height:50px;border:2.5px solid var(--heading);border-radius:50%;display:flex;align-items:center;justify-content:center;font-family:Montserrat,sans-serif;font-size:20px;color:var(--heading)}
.date-label{position:absolute;left:6px;top:54px;font-size:7.5px;color:var(--heading)}
.news-item h4{position:absolute;left:59px;top:4px;font-size:11.5px;font-weight:700;color:var(--heading)}
.news-item p{position:absolute;left:59px;top:21px;width:225px;font-size:8.8px;line-height:11.5px}
.news-item a{position:absolute;left:59px;top:59px;font-size:7.5px;color:var(--navy);text-decoration:none}

/* info columns */
.info h2{font-family:Montserrat,sans-serif;font-weight:500;font-size:15px;color:var(--ink);margin-bottom:8px}
.info p{font-size:8.8px;line-height:11.6px;color:var(--navy)}
.info{position:absolute;top:877px;width:206px}
.info-photo{float:left;width:114px;height:78px;margin:0 8px 4px 0}
.read-btn{display:inline-block;margin-top:10px;width:88px;height:31px;background:var(--navy);color:var(--white);font-size:9.5px;line-height:31px;text-align:center}

/* footer */
.footer{left:0;top:1096px;width:814px;height:104px;background:var(--pale)}
.foot-h{font-family:Montserrat,sans-serif;font-size:11.5px;color:var(--ink)}
.foot-links{font-size:7.8px;line-height:12px;color:var(--ink);list-style:none}
.email{left:297px;top:1139px;width:157px;height:20px;background:var(--white);font-size:9px;padding:5px 7px;color:#333}
.go{left:458px;top:1139px;width:27px;height:20px;background:#5e6a7a;color:var(--white);font-size:9px;text-align:center;line-height:20px}
.social{left:588px;top:1118px;display:flex;gap:9px}
.social span{width:15px;height:15px;border-radius:50%;background:var(--ink)}
.copy{left:587px;top:1144px;font-size:7.5px;color:var(--ink)}
.call{left:587px;top:1157px;font-size:12px;color:var(--ink)}
</style>
</head>
<body>

<header>
  <div class="abs brand"><span class="brand-dot"></span><span class="brand-name">Qolvine Enterprises</span></div>
  <nav class="abs main-nav">
    <a class="current" href="#">HOME</a><a href="#">ABOUT US</a><a href="#">SERVICES</a><a href="#">LATEST NEWS</a><a href="#">CONTACT US</a>
  </nav>
</header>

<section>
  <div class="abs sky-band"></div>
  <div class="abs hero-frame"></div>
  <div class="abs hero-photo" role="img" aria-label="Business team meeting around an office table"></div>
  <div class="abs hero-caption"></div>
  <div class="abs hero-title">INVESTMENT PHILOSOPHY</div>
  <div class="abs hero-text">Duis aute irure dolor in reprehenderit in voluptate velit esse cillum dolore eu fugiat nulla pariatur.</div>
  <div class="abs learn-btn">LEARN MORE ›</div>
</section>

<section class="abs services">
  <div class="service" style="left:88px">
    <svg width="40" height="34" viewBox="0 0 40 34" fill="none" stroke="#fff" stroke-width="3" stroke-linecap="round"><circle cx="18" cy="4" r="3" fill="#fff" stroke="none"/><path d="M16 9l-4 10 8 3-3 10M16 9l8 4 6-3M12 19l-7 6"/><path d="M8 30l10-6 8 4 12-12M33 16h5v5" stroke-width="2"/></svg>
    <h3>PRODUCT DEVELOPMENT</h3>
    <p>Lorem ipsum dolor sit amet, consectetur adipisicing elit, sed do eiusmod tempor incididunt ut labore et dolore magna aliqua.</p>
  </div>
  <div class="service" style="left:310px">
    <svg width="40" height="34" viewBox="0 0 40 34" fill="#fff"><circle cx="14" cy="5" r="4"/><path d="M8 11h12v14h-3v9h-6v-9H8z"/><circle cx="26" cy="23" r="9" fill="none" stroke="#fff" stroke-width="2"/><text x="26" y="27" font-size="11" text-anchor="middle" font-family="Arial">$</text></svg>
    <h3>SALES/BROKER</h3>
    <p>Duis aute irure dolor in reprehenderit in voluptate velit esse cillum dolore eu fugiat nulla pariatur. Excepteur sint occaecat cupidatat non proident.</p>
  </div>
  <div class="service" style="left:531px">
    <svg width="40" height="34" viewBox="0 0 40 34" fill="#fff"><circle cx="20" cy="4" r="3.5"/><path d="M16 9h8v13h-8z"/><circle cx="9" cy="9" r="3"/><path d="M6 13h6v10H6z"/><circle cx="31" cy="9" r="3"/><path d="M28 13h6v10h-6z"/><ellipse cx="20" cy="28" rx="17" ry="4" fill="none" stroke="#fff" stroke-width="2"/></svg>
    <h3>IMPORT/EXPORT</h3>
    <p>Sed ut perspiciatis, unde omnis iste natus error sit voluptatem accusantium doloremque laudantium, totam rem aperiam eaque ipsa, quae ab illo.</p>
  </div>
</section>

<section>
  <div class="abs news"></div>
  <h2 class="abs news-title">LATEST NEWS</h2>
  <a class="abs news-more">more news</a>
  <div class="abs news-rule"></div>

  <article class="news-item" style="left:93px;top:607px"><div class="date-ring">30</div><div class="date-label">JUL, 2014</div><h4>At vero eos et accusamus et iusto</h4><p>Odio dignissimos duaccimus qui bland ditiis praesentium voluptatum deleniti atque corrupti quos dolores et.</p><a href="#">read more</a></article>
  <article class="news-item" style="left:438px;top:607px"><div class="date-ring">30</div><div class="date-label">JUL, 2014</div><h4>At vero eos et accusamus et iusto</h4><p>Odio dignissimos duaccimus qui bland ditiis praesentium voluptatum deleniti atque corrupti quos dolores et.</p><a href="#">read more</a></article>
  <article class="news-item" style="left:93px;top:712px"><div class="date-ring">30</div><div class="date-label">JUL, 2014</div><h4>At vero eos et accusamus et iusto</h4><p>Odio dignissimos duaccimus qui bland ditiis praesentium voluptatum deleniti atque corrupti quos dolores et.</p><a href="#">read more</a></article>
  <article class="news-item" style="left:438px;top:712px"><div class="date-ring">30</div><div class="date-label">JUL, 2014</div><h4>At vero eos et accusamus et iusto</h4><p>Odio dignissimos duaccimus qui bland ditiis praesentium voluptatum deleniti atque corrupti quos dolores et.</p><a href="#">read more</a></article>
</section>

<section>
  <div class="info" style="left:83px">
    <h2>Who Choose Us</h2>
    <p>Lorem ipsum dolor sit amet, consectetur adipisicing elit, sed do eiusmod tempor incididunt ut labore et dolore magna aliqua.</p>
    <p style="margin-top:10px">Ut enim ad minim veniam, quis nostrud exercitation ullamco laboris nisi ut aliquip ex ea commodo consequat. Duis aute irure dolor in reprehenderit in voluptate velit esse cillum dolore eu fugiat nulla pariatur.</p>
    <span class="read-btn">read more</span>
  </div>
  <div class="info" style="left:301px;width:212px">
    <h2>Experiences</h2>
    <div class="info-photo" role="img" aria-label="Three business professionals standing together" style="background:linear-gradient(160deg,#eef1f3,#9aa3ab 55%,#2f3540)"></div>
    <p>Lorem ipsum dolor sit amet, consectetur adipisicing elit, sed do eiusmod tempor incididunt ut labore et dolore magna aliqua.</p>
    <p style="clear:both;padding-top:6px">Ut enim ad minim veniam, quis nostrud exercitation ullamco laboris nisi ut aliquip ex ea commodo consequat. Duis aute irure dolor in reprehenderit in voluptate velit esse cillum dolore eu fugiat nulla pariatur.</p>
  </div>
  <div class="info" style="left:524px;width:212px">
    <h2>About Qolvine</h2>
    <div class="info-photo" role="img" aria-label="Business team posing in an office" style="background:linear-gradient(160deg,#f2f2f2,#a7adb3 50%,#26292f)"></div>
    <p>Lorem ipsum dolor sit amet, consectetur adipisicing elit, sed do eiusmod tempor incididunt ut labore et dolore magna aliqua.</p>
    <p style="clear:both;padding-top:6px">Ut enim ad minim veniam, quis nostrud exercitation ullamco laboris nisi ut aliquip ex ea commodo consequat. Duis aute irure dolor in reprehenderit in voluptate velit esse cillum dolore eu fugiat nulla pariatur.</p>
  </div>
</section>

<footer>
  <div class="abs footer"></div>
  <div class="abs foot-h" style="left:78px;top:1115px">Navigation</div>
  <ul class="abs foot-links" style="left:78px;top:1135px"><li>Home</li><li>Who we are</li><li>What we do</li></ul>
  <ul class="abs foot-links" style="left:153px;top:1135px"><li>Who we serve</li><li>Education</li><li>Contact us</li></ul>
  <div class="abs foot-h" style="left:297px;top:1115px">Newsltter Signup</div>
  <div class="abs email">enter email</div>
  <div class="abs go">go</div>
  <div class="abs social"><span></span><span></span><span></span><span></span></div>
  <div class="abs copy">Copyright © 2014 | Terms | Privacy</div>
  <div class="abs call">CALL US: 1 800 555 0142</div>
</footer>

</body>
</html>
```